Fatigued and Overloaded by COVID Messages? We need original illustrations to show that.

Everywhere you look there are messages about COVID. That is leading many people to feel fatigued and overloaded by the messages.

We surveyed U.S. adults March 20th - 24th, 2020 and measured message fatigue, information overload, perceived repetition, and perceived exaggeration. Here is how participants responded:

When it comes to coronavirus . . .
55% feel exhausted by all the messages.
54% feel overloaded by the amount of information.
51% feel that the messages are repetitive.
47% feel like messages exaggerate how bad it is.

In other words, almost half of U.S. adults show signs of message fatigue, information overload, perceived message repetition, and perceived message exaggeration.

We will continue to survey 400 adults every week for the next 16 weeks. Each time we will measure message fatigue, information overload, perceived repetition, and perceived exaggeration. We expect that it will increase over time.

What are we looking for? We need innovative and original illustrations that attempt to communicate these findings. The illustrations would visualize message fatigue, information overload, perceived message repetition, and perceived message exaggeration.

What sort of visual are we looking for? Our preference is for an original illustration (or set of illustrations). Our preference is for creative and powerful illustrations, but we are also open to the creative and well-executed infographics.

We need these images fast . We will award monetary prizes to the 3 best designs. If we like more than that, then we might purchase more (e.g., in past contests, we have purchased as many as 30 designs).

What we will need:
(1) The illustrations must be original and we will need the photoshop and/or illustrator files for all artwork. (By original, we mean that the illustrations are 100% created by you. Our organization requires that we utilize only original illustrated work. We have had issues with free imagery being pirated and reposted as free. We sidestep that issue by just having everything created.)

(2) The illustration should say, somewhere: "Based on a survey of 400 U.S. adults conducted March 20 - 24th, 2020."

(3) We will have almost 4 months worth of data by the time this is done. In other words, the illustrations might be able to help us present that weekly data.

(4) We have conducted other Artvendo projects. It might be helpful to examine designs we liked in the past. For example, here is another COVID project we just finished:

https://jobs.artvendo-example.com/job/5162048

Target Market(s)

U.S. adults

Requirements
Must have
• Original illustrations. Mobile friendly design. People will view this on their smartphones.
Nice to have
• A design that we can use to communicate the data across time.

```html
<!DOCTYPE html>
<html lang="en">
<head>
<meta charset="utf-8">
<title>When It Comes To Coronavirus – Message Fatigue Survey</title>
<link rel="stylesheet" href="https://fonts.googleapis.com/css2?family=Arimo:wght@400;700&family=Oswald:wght@500&family=Creepster&display=swap">
<style>
  :root {
    --white: #ffffff;
    --ink: #111111;
    --red: #ec1c24;
    --orange: #f3922a;
    --yellow: #f5de2e;
    --amber: #f7b325;
    --lemon: #f8ef1c;
    --sky: #36c3da;
    --ocean: #2aa5d8;
    --card-blue: #4aa3dc;
    --note: #f7f2a8;
    --note-shade: #c49a2c;
    --virus-light: #52c24a;
    --virus-dark: #11803c;
    --flag-navy: #3d3a6b;
    --flag-red: #b11e32;
  }
  html, body { margin: 0; padding: 0; overflow: hidden; background: var(--white); }
  .poster { display: block; width: 1200px; height: 1200px; }
  .headline { font-family: "Arimo", Arial, sans-serif; font-weight: 700; font-size: 36px; fill: var(--ink); }
  .virus-word { font-family: "Creepster", "Arimo", sans-serif; font-size: 44px; fill: var(--white); letter-spacing: 1px; }
  .stat-number { font-family: "Arimo", Arial, sans-serif; font-size: 80px; fill: var(--white); }
  .note-label { font-family: "Arimo", Arial, sans-serif; font-weight: 700; fill: var(--ink); }
  .finding { font-family: "Arimo", Arial, sans-serif; font-weight: 700; font-size: 24px; fill: var(--ink); }
  .source-line { font-family: "Oswald", "Arial Narrow", sans-serif; font-weight: 500; font-size: 38px; fill: var(--white); }
</style>
</head>
<body>
<svg class="poster" viewBox="0 0 1200 1200" xmlns="http://www.w3.org/2000/svg">
  <defs>
    <linearGradient id="band-warm" x1="0" y1="0" x2="0" y2="1">
      <stop offset="0" stop-color="var(--yellow)"/>
      <stop offset="1" stop-color="var(--amber)"/>
    </linearGradient>
    <linearGradient id="band-sea" x1="0" y1="0" x2="1" y2="1">
      <stop offset="0" stop-color="var(--ocean)"/>
      <stop offset="0.5" stop-color="var(--sky)"/>
      <stop offset="1" stop-color="var(--ocean)"/>
    </linearGradient>
    <radialGradient id="virus-tone">
      <stop offset="0.55" stop-color="var(--virus-light)"/>
      <stop offset="1" stop-color="var(--virus-dark)"/>
    </radialGradient>
    <linearGradient id="map-tone" x1="0" y1="0" x2="1" y2="0">
      <stop offset="0" stop-color="var(--flag-navy)"/>
      <stop offset="0.45" stop-color="var(--flag-navy)"/>
      <stop offset="0.55" stop-color="var(--flag-red)"/>
      <stop offset="1" stop-color="var(--flag-red)"/>
    </linearGradient>
  </defs>

  <!-- background bands -->
  <rect class="bg-top" width="1200" height="1200" fill="var(--white)"/>
  <path class="band-warm" d="M0 205 Q600 430 1200 248 V1200 H0 Z" fill="url(#band-warm)" stroke="var(--orange)" stroke-width="8"/>
  <path class="band-sea" d="M0 950 Q600 640 1200 913 V1200 H0 Z" fill="url(#band-sea)" stroke="var(--lemon)" stroke-width="8"/>

  <!-- virus decorations -->
  <circle role="img" aria-label="Green coronavirus particle illustration" cx="93" cy="84" r="62" fill="url(#virus-tone)"/>
  <circle role="img" aria-label="Small green coronavirus particle illustration" cx="260" cy="51" r="26" fill="url(#virus-tone)"/>
  <circle role="img" aria-label="Green coronavirus particle illustration" cx="433" cy="70" r="53" fill="url(#virus-tone)"/>
  <circle role="img" aria-label="Green coronavirus particle illustration" cx="271" cy="200" r="59" fill="url(#virus-tone)"/>

  <!-- headline -->
  <text class="headline" x="427" y="169">WHEN IT COMES TO</text>
  <path class="headline-arrow" d="M426 180 H792 V161 L820 188 L792 214 V197 H426 Z" fill="var(--red)"/>
  <circle role="img" aria-label="Large green coronavirus particle illustration" cx="1006" cy="165" r="150" fill="url(#virus-tone)"/>
  <text class="virus-word" x="1008" y="182" text-anchor="middle" textLength="210" lengthAdjust="spacingAndGlyphs">CORONAVIRUS</text>

  <!-- stat cards -->
  <g class="stat-card">
    <rect x="25" y="432" width="264" height="248" rx="52" fill="var(--card-blue)" stroke="var(--white)" stroke-width="8"/>
    <path class="note-shadow" d="M74 480 L236 478 L242 646 L80 640 Z" fill="var(--note-shade)" opacity="0.6"/>
    <path class="note" d="M70 476 L229 476 L236 638 L70 635 Z" fill="var(--note)"/>
    <circle class="pin" cx="152" cy="484" r="12" fill="var(--red)"/>
    <text class="note-label" x="151" y="549" font-size="23" text-anchor="middle">MESSAGE</text>
    <text class="note-label" x="149" y="579" font-size="23" text-anchor="middle">FATIGUE</text>
    <ellipse cx="149" cy="376" rx="106" ry="88" fill="var(--red)" stroke="var(--ink)" stroke-width="5"/>
    <text class="stat-number" x="149" y="410" text-anchor="middle">55%</text>
    <text class="finding" x="163" y="723" text-anchor="middle">FEEL EXHAUSTED</text>
    <text class="finding" x="160" y="749" text-anchor="middle">BY ALL THE</text>
    <text class="finding" x="160" y="775" text-anchor="middle">MESSAGES.</text>
  </g>

  <g class="stat-card">
    <rect x="338" y="432" width="267" height="246" rx="52" fill="var(--card-blue)" stroke="var(--white)" stroke-width="8"/>
    <path class="note-shadow" d="M374 488 L550 486 L558 654 L380 648 Z" fill="var(--note-shade)" opacity="0.6"/>
    <path class="note" d="M370 484 L545 484 L552 646 L370 644 Z" fill="var(--note)"/>
    <circle class="pin" cx="462" cy="493" r="12" fill="var(--red)"/>
    <text class="note-label" x="463" y="559" font-size="21" text-anchor="middle">INFORMATION</text>
    <text class="note-label" x="460" y="588" font-size="21" text-anchor="middle">OVERLOAD</text>
    <ellipse cx="469" cy="382" rx="105" ry="88" fill="var(--red)" stroke="var(--ink)" stroke-width="5"/>
    <text class="stat-number" x="474" y="422" text-anchor="middle">54%</text>
    <text class="finding" x="451" y="716" text-anchor="middle">FEEL OVERLOADED</text>
    <text class="finding" x="451" y="742" text-anchor="middle">BY THE AMOUNT OF</text>
    <text class="finding" x="451" y="768" text-anchor="middle">INFORMATION.</text>
  </g>

  <g class="stat-card">
    <rect x="645" y="434" width="265" height="244" rx="52" fill="var(--card-blue)" stroke="var(--white)" stroke-width="8"/>
    <path class="note-shadow" d="M703 480 L876 478 L884 646 L706 640 Z" fill="var(--note-shade)" opacity="0.6"/>
    <path class="note" d="M699 476 L871 476 L878 638 L699 635 Z" fill="var(--note)"/>
    <circle class="pin" cx="789" cy="484" r="12" fill="var(--red)"/>
    <text class="note-label" x="787" y="559" font-size="23" text-anchor="middle">PERCEIVED</text>
    <text class="note-label" x="787" y="589" font-size="23" text-anchor="middle">MESSAGE</text>
    <ellipse cx="778" cy="380" rx="104" ry="88" fill="var(--red)" stroke="var(--ink)" stroke-width="5"/>
    <text class="stat-number" x="785" y="418" text-anchor="middle">51%</text>
    <text class="finding" x="768" y="710" text-anchor="middle">FEEL THAT THE</text>
    <text class="finding" x="768" y="736" text-anchor="middle">MESSAGES ARE</text>
    <text class="finding" x="768" y="762" text-anchor="middle">REPETITIVE.</text>
  </g>

  <g class="stat-card">
    <rect x="945" y="435" width="249" height="243" rx="52" fill="var(--card-blue)" stroke="var(--white)" stroke-width="8"/>
    <path class="note-shadow" d="M997 492 L1157 490 L1165 656 L1000 650 Z" fill="var(--note-shade)" opacity="0.6"/>
    <path class="note" d="M993 488 L1152 488 L1158 650 L993 647 Z" fill="var(--note)"/>
    <circle class="pin" cx="1076" cy="496" r="12" fill="var(--red)"/>
    <text class="note-label" x="1073" y="565" font-size="17" text-anchor="middle">MESSAGE</text>
    <text class="note-label" x="1071" y="595" font-size="17" text-anchor="middle">EXAGGERATION</text>
    <ellipse cx="1067" cy="388" rx="104" ry="88" fill="var(--red)" stroke="var(--ink)" stroke-width="5"/>
    <text class="stat-number" x="1072" y="422" text-anchor="middle">47%</text>
    <text class="finding" x="1053" y="717" text-anchor="middle">FEEL LIKE</text>
    <text class="finding" x="1053" y="743" text-anchor="middle">MESSAGES</text>
    <text class="finding" x="1053" y="769" text-anchor="middle">EXAGGERATE HOW</text>
    <text class="finding" x="1053" y="795" text-anchor="middle">BAD IT IS.</text>
  </g>

  <!-- country map -->
  <rect role="img" aria-label="Map of the United States filled with the stars and stripes of the U.S. flag" x="385" y="807" width="491" height="298" rx="40" fill="url(#map-tone)" opacity="0.9"/>

  <!-- source line -->
  <text class="source-line" x="25" y="1155" textLength="1124" lengthAdjust="spacingAndGlyphs">BASED ON A SURVEY OF 400 U.S. ADULTS CONDUCTED MARCH 20 - 24TH, 2020</text>
</svg>
</body>
</html>
```